Veltrano - Mechanic/Collision Center Business Card

We're looking for a business card design for our mechanic/ collision repair shop.

Can be with colours or monochromatic.

See the attached files.

Many thanks

```html
<!DOCTYPE html>
<html lang="en">
<head>
<meta charset="utf-8">
<title>Veltrano – Business Cards</title>
<link href="https://fonts.googleapis.com/css2?family=Arimo:wght@400;700&display=swap" rel="stylesheet">
<style>
  :root {
    --page-bg: #e8eceb;
    --card-bg: #ffffff;
    --brand-blue: #45c3f3;
    --brand-grey: #6e7b80;
    --text-grey: #4a5053;
    --mark-dark: #1d1f20;
    --white: #ffffff;
  }
  * { margin: 0; padding: 0; box-sizing: border-box; }
  html, body {
    width: 849px; height: 1200px; overflow: hidden;
    background: var(--page-bg);
    font-family: "Arimo", Arial, sans-serif;
  }
  .sheet { position: relative; width: 849px; height: 1200px; }
  .card {
    position: absolute; left: 148px; width: 558px; height: 319px;
    background: var(--card-bg); overflow: hidden;
  }
  .card--front { top: 63px; }
  .card--person { top: 441px; height: 320px; }
  .card--company { top: 823px; }

  .stripe-grey { position: absolute; left: 0; width: 100%; height: 11px; background: var(--brand-grey); }
  .stripe-blue { position: absolute; left: 0; width: 100%; background: var(--brand-blue); }
  .card--front .stripe-grey { top: 275px; }
  .card--front .stripe-blue { top: 295px; height: 24px; }
  .card--person .stripe-grey, .card--company .stripe-grey { top: 233px; }
  .card--person .stripe-blue, .card--company .stripe-blue { top: 252px; height: 68px; }

  .brand-mark {
    position: absolute; display: flex; align-items: center; justify-content: center;
    gap: 10px; color: var(--mark-dark); font-weight: 700; letter-spacing: 1px;
  }
  .brand-mark__square { background: var(--brand-blue); flex: none; }
  .card--front .brand-mark { left: 0; width: 100%; top: 105px; font-size: 58px; }
  .card--front .brand-mark__square { width: 40px; height: 40px; }
  .card--person .brand-mark { left: 335px; width: 200px; top: 60px; font-size: 26px; gap: 7px; }
  .card--company .brand-mark { left: 342px; width: 200px; top: 58px; font-size: 26px; gap: 7px; }
  .brand-mark--small .brand-mark__square { width: 18px; height: 18px; }

  .contact { position: absolute; left: 44px; color: var(--text-grey); font-size: 19px; line-height: 24px; }
  .contact__name { color: var(--brand-blue); font-weight: 700; font-size: 29px; line-height: 34px; margin-bottom: 10px; }
  .card--company .contact__name { font-size: 30px; margin-bottom: 18px; }
  .contact__lines { margin-top: 13px; padding-left: 3px; }
  .card--company .contact__lines { margin-top: 24px; padding-left: 0; }
  .card--person .contact { top: 28px; }
  .card--company .contact { top: 31px; }

  .social { position: absolute; left: 44px; top: 266px; display: flex; align-items: center; }
  .social__badge {
    width: 119px; height: 39px; border: 1.5px solid var(--white); border-radius: 2px;
    display: flex; align-items: center; justify-content: center; gap: 6px;
    color: var(--white); font-weight: 700; font-size: 16px;
  }
  .social__badge-square { width: 14px; height: 14px; background: var(--white); }
  .social__url { margin-left: 20px; color: var(--white); font-size: 19px; letter-spacing: 0.8px; }
</style>
</head>
<body>
<main class="sheet">

  <section class="card card--front" aria-label="Card front">
    <div class="brand-mark"><span class="brand-mark__square"></span>VELTRANO</div>
    <div class="stripe-grey"></div>
    <div class="stripe-blue"></div>
  </section>

  <section class="card card--person" aria-label="Personal card back">
    <div class="contact">
      <h1 class="contact__name">Rui Matos</h1>
      <p>Rua das Oficinas, 42<br>1900-214 Lisboa</p>
      <p class="contact__lines">Mobile: +351 910000482<br>Phone: +351 210004715<br>Email: veltrano.oficina@mailbox.pt</p>
    </div>
    <div class="brand-mark brand-mark--small"><span class="brand-mark__square"></span>VELTRANO</div>
    <div class="stripe-grey"></div>
    <div class="stripe-blue"></div>
    <div class="social">
      <div class="social__badge"><span class="social__badge-square"></span>Chatterly</div>
      <span class="social__url">www.chatterly.com/veltrano</span>
    </div>
  </section>

  <section class="card card--company" aria-label="Company card back">
    <div class="contact">
      <h2 class="contact__name">Veltrano, LDA</h2>
      <p>Rua das Oficinas, 42<br>1900-214 Lisboa</p>
      <p class="contact__lines">Phone: +351 210004715<br>Email: veltrano.oficina@mailbox.pt</p>
    </div>
    <div class="brand-mark brand-mark--small"><span class="brand-mark__square"></span>VELTRANO</div>
    <div class="stripe-grey"></div>
    <div class="stripe-blue"></div>
    <div class="social">
      <div class="social__badge"><span class="social__badge-square"></span>Chatterly</div>
      <span class="social__url">www.chatterly.com/veltrano</span>
    </div>
  </section>

</main>
</body>
</html>
```